Wool Product Label / Yarn Band

Looking to update the packaging on our wool products. This includes a design for a paper band to place around braided wool or yarn, and a design for a sticker to place on the outside of tissue paper wrapping. Open to updating or modifying the logo, which does not fit well on a round sticker, but the sticker could also be something wool related (like a sheep or drop spindle) that does not include the logo.
Target Market(s)
Wool crafters (knitters / spinners / felters). Mainly women, aged 30-70
Industry/Entity Type
Textile
Colors
Designer to choose colors to be used in the design.
Requirements
Must have
- Band needs to include, brand name, logo, url (fernloomstead.com), dyelot number, as well as the fiber content (ex: Merino Wool) and weight of the fiber (ex: 4oz).
Nice to have
- Band would ideally be easily customized because the weight and fiber content is variable and will be printed specifically for each product, Variable information can be on a sticker or printed directly on a band that can be printed on a standard printer. Attached is a photo of the current band and it's application.

```html
<!DOCTYPE html>
<html lang="en">
<head>
<meta charset="utf-8">
<title>Fernloomstead – Sticker and Yarn Band</title>
<link rel="stylesheet" href="https://fonts.googleapis.com/css2?family=Montserrat:wght@400;600;700&display=swap">
<style>
  :root {
    --stage-top: #5a5a5a;
    --stage-bottom: #8e8e8e;
    --paper: #ffffff;
    --violet: #45339a;
    --magenta: #a8358f;
    --crimson: #d8202e;
    --wine: #9b1c1f;
    --navy: #2b3590;
    --knit-blue: #2a4fa8;
    --knit-cream: #e9d9bf;
    --knit-red: #e32228;
    --sheep-tone: rgba(255,255,255,0.28);
  }
  html, body {
    margin: 0;
    width: 1200px;
    height: 1200px;
    overflow: hidden;
  }
  body {
    background: linear-gradient(to bottom, var(--stage-top) 0%, var(--stage-top) 45%, var(--stage-bottom) 100%);
    font-family: "Montserrat", sans-serif;
    position: relative;
  }
  .sticker {
    position: absolute;
    border-radius: 50%;
    background: var(--paper);
  }
  .sticker-face {
    position: absolute;
    border-radius: 50%;
    background: linear-gradient(to right, var(--violet) 0%, var(--magenta) 50%, var(--crimson) 100%);
    display: flex;
    flex-direction: column;
    align-items: center;
    justify-content: center;
  }
  .sheep-art {
    border-radius: 40% 45% 30% 30%;
    background: var(--sheep-tone);
  }
  .brand-name {
    color: var(--paper);
    font-weight: 600;
    letter-spacing: -0.5px;
    line-height: 1;
  }

  /* standalone sticker */
  .sticker--large { left: 154px; top: 348px; width: 478px; height: 478px; }
  .sticker--large .sticker-face { left: 12px; top: 12px; width: 454px; height: 454px; }
  .sticker--large .sheep-art { width: 130px; height: 110px; margin-bottom: 22px; }
  .sticker--large .brand-name { font-size: 46px; }

  /* yarn band */
  .yarn-band {
    position: absolute;
    left: 705px; top: 104px;
    width: 321px; height: 991px;
    background: var(--paper);
  }
  .knit-strip {
    position: absolute;
    top: 0; bottom: 0;
    width: 75px;
  }
  .knit-strip--left {
    left: 0;
    background: linear-gradient(to right, #f4f4f4 0%, #f4f4f4 40%, var(--knit-blue) 45%, var(--knit-blue) 70%, var(--knit-cream) 75%, var(--knit-cream) 100%);
  }
  .knit-strip--right {
    right: 0;
    background: linear-gradient(to right, var(--knit-blue) 0%, var(--knit-blue) 8%, #f4f4f4 12%, #f4f4f4 30%, var(--knit-red) 35%, var(--knit-red) 100%);
  }
  .band-panel {
    position: absolute;
    left: 75px; top: 0;
    width: 167px; height: 987px;
    border: 2px solid var(--wine);
    background: var(--paper);
  }
  .sticker--band {
    left: 12px; top: 306px;
    width: 298px; height: 298px;
    box-shadow: 0 0 26px rgba(0,0,0,0.22);
  }
  .sticker--band .sticker-face { left: 7px; top: 7px; width: 284px; height: 284px; }
  .sticker--band .sheep-art { width: 82px; height: 70px; margin-bottom: 14px; }
  .sticker--band .brand-name { font-size: 29px; }

  .band-details {
    position: absolute;
    left: 164px; top: 765px;
    width: 420px;
    transform: translate(-50%, -50%) rotate(-90deg);
    text-align: center;
    color: var(--wine);
    font-size: 15px;
    font-weight: 400;
  }
  .band-details p { margin: 0; line-height: 29px; }
  .band-details strong { font-weight: 700; }
  .band-details .band-url {
    color: var(--navy);
    margin-top: 14px;
    font-size: 16px;
  }
</style>
</head>
<body>

  <div class="sticker sticker--large">
    <div class="sticker-face">
      <div class="sheep-art" role="img" aria-label="Engraved illustration of a standing sheep"></div>
      <span class="brand-name">Fernloomstead</span>
    </div>
  </div>

  <div class="yarn-band">
    <div class="knit-strip knit-strip--left" role="img" aria-label="Knit stitch pattern in white, blue and cream"></div>
    <div class="knit-strip knit-strip--right" role="img" aria-label="Knit stitch pattern in red and white"></div>
    <div class="band-panel"></div>

    <div class="sticker sticker--band">
      <div class="sticker-face">
        <div class="sheep-art" role="img" aria-label="Engraved illustration of a standing sheep"></div>
        <span class="brand-name">Fernloomstead</span>
      </div>
    </div>

    <div class="band-details">
      <p><strong>85%</strong> Merino Wool | <strong>15%</strong> Silk</p>
      <p>Qty : <strong>4.0</strong> oz</p>
      <p>S/N : MER/SILK-BLEND1</p>
      <p class="band-url">www.fernloomstead.com</p>
    </div>
  </div>

</body>
</html>
```